Larvik Consulting

Hi,
I have my own network consulting business (just me)
and need to get a logo and business card design together,

Based in New Zealand,

Tobias Wrenfield
Unified Communications and Network Architect

/design engineer,
and would like this to be the basis for personal branding and company identity

Industry/Entity Type

Business

Requirements
Nice to have
• I have the basis for a optional logo - needs color -

```html
<!DOCTYPE html>
<html lang="en">
<head>
<meta charset="utf-8">
<title>Larvik Consulting – Business Card</title>
<link rel="stylesheet" href="https://fonts.googleapis.com/css2?family=Mulish:wght@400;600;800&display=swap">
<style>
  :root {
    --stage: #2b2b2b;
    --card-white: #ffffff;
    --card-grey: #e6e6e6;
    --brand-blue: #1ba7e1;
    --brand-blue-light: #7cd0f3;
    --brand-blue-deep: #0f93cf;
    --ink: #3a3a3a;
    --ink-soft: #555555;
  }
  * { box-sizing: border-box; margin: 0; padding: 0; }
  html, body {
    width: 1200px; height: 1200px; overflow: hidden;
    background: var(--stage);
    font-family: "Mulish", "Helvetica Neue", Arial, sans-serif;
  }
  .canvas {
    position: relative; width: 1200px; height: 1200px;
  }
  .card {
    position: absolute; left: 150px;
    width: 900px; height: 514px;
    overflow: hidden;
    box-shadow: 0 18px 40px rgba(0,0,0,.45);
  }
  /* Front */
  .card--front {
    top: 64px;
    background: linear-gradient(160deg, var(--card-white) 35%, var(--card-grey) 100%);
  }
  .brand {
    position: absolute; left: 96px; top: 110px;
    display: flex; align-items: center; gap: 22px;
  }
  .brand__dot {
    width: 64px; height: 64px; border-radius: 50%;
    background: var(--brand-blue);
  }
  .brand__name {
    font-weight: 800; font-size: 50px; line-height: 1;
    letter-spacing: 1px; text-transform: uppercase;
    color: var(--brand-blue);
  }
  .person {
    position: absolute; left: 96px; top: 300px;
  }
  .person__name {
    font-weight: 800; font-size: 42px; line-height: 1;
    color: var(--brand-blue);
  }
  .person__role {
    font-weight: 400; font-size: 21px; margin-top: 4px;
    color: var(--ink); text-align: right;
  }
  .contact {
    position: absolute; display: flex; align-items: center; gap: 9px;
    font-size: 18px; font-weight: 600; color: var(--ink);
  }
  .contact svg { width: 20px; height: 20px; fill: none; stroke: var(--ink-soft); stroke-width: 1.8; }
  .contact--phone { left: 450px; top: 338px; }
  .contact--web { left: 640px; top: 338px; }
  .contact--email { left: 96px; top: 448px; }
  .band {
    position: absolute; left: 0; right: 0; top: 378px; height: 40px;
    background: linear-gradient(180deg, var(--brand-blue-light), var(--brand-blue));
  }
  /* Back */
  .card--back {
    top: 622px;
    background: var(--brand-blue);
  }
  .card__pattern {
    position: absolute; inset: 0;
    background: radial-gradient(circle at 70% 25%, var(--brand-blue-light) 0%, var(--brand-blue) 55%, var(--brand-blue-deep) 100%);
  }
  .back-brand {
    position: absolute; inset: 0;
    display: flex; align-items: center; justify-content: center; gap: 20px;
  }
  .back-brand__dot {
    width: 56px; height: 56px; border-radius: 50%; background: var(--card-white);
  }
  .back-brand__name {
    font-weight: 800; font-size: 44px; letter-spacing: 1px;
    text-transform: uppercase; color: var(--card-white);
  }
</style>
</head>
<body>
<main class="canvas">
  <section class="card card--front" aria-label="Business card front">
    <div class="brand">
      <span class="brand__dot"></span>
      <span class="brand__name">Larvik Consulting</span>
    </div>

    <div class="person">
      <p class="person__name">Tobias Wrenfield</p>
      <p class="person__role">design engineer</p>
    </div>

    <p class="contact contact--phone">
      <svg viewBox="0 0 24 24"><path d="M6 3h3l2 5-2.5 1.5a11 11 0 0 0 6 6L16 13l5 2v3a3 3 0 0 1-3 3A15 15 0 0 1 3 6a3 3 0 0 1 3-3z"/></svg>
      001 555 010 204
    </p>
    <p class="contact contact--web">
      <svg viewBox="0 0 24 24"><circle cx="12" cy="12" r="9"/><path d="M3 12h18M12 3c3 3 3 15 0 18M12 3c-3 3-3 15 0 18"/></svg>
      www.larvikconsulting.nz
    </p>

    <div class="band"></div>

    <p class="contact contact--email">
      <svg viewBox="0 0 24 24"><rect x="3" y="5" width="18" height="14"/><path d="M3 5l9 8 9-8"/></svg>
      tobias@larvikconsulting.nz
    </p>
  </section>

  <section class="card card--back" aria-label="Business card back">
    <div class="card__pattern" role="img" aria-label="Repeating light blue decorative pattern across the card back"></div>
    <div class="back-brand">
      <span class="back-brand__dot"></span>
      <span class="back-brand__name">Larvik Consulting</span>
    </div>
  </section>
</main>
</body>
</html>
```